business card design

i would like business cards designed. My business provides trade qualified personnel to the mining industry to work on heavy mobile equipment.
please put a excavator(digger) in the background in one design and have one design without so i can compare the difference.
also add info:
my logo(attached) and "mobile equipment repair and maintenance"
name: Derek Holloway
address: 57 Tarrowby RD Wendale Norvick QX.
mobile: 0438120957
email: derek@ironvalemx.com

```html
<!DOCTYPE html>
<html lang="en">
<head>
<meta charset="utf-8">
<title>Ironvale Maintenance Services – Business Cards</title>
<link href="https://fonts.googleapis.com/css2?family=Poppins:wght@400;500;600;700;800&display=swap" rel="stylesheet">
<style>
  :root {
    --navy: #0f2350;
    --navy-deep: #0a1a3d;
    --blue: #1f7ae6;
    --blue-bright: #2b8cff;
    --white: #ffffff;
    --stage: #2a2a2c;
    --rock: #6f7680;
    --machine: #d9951c;
  }
  * { box-sizing: border-box; margin: 0; padding: 0; }
  html, body {
    width: 1200px; height: 900px; overflow: hidden;
    background: var(--stage);
    font-family: "Poppins", sans-serif;
  }
  .sheet {
    position: relative; width: 1200px; height: 900px;
    display: flex; flex-direction: column; align-items: center; justify-content: center; gap: 40px;
  }
  .card {
    position: relative; width: 700px; height: 400px;
    border-radius: 22px; overflow: hidden;
    background: linear-gradient(135deg, var(--navy) 0%, var(--navy-deep) 100%);
    box-shadow: 0 14px 30px rgba(0,0,0,.45);
  }

  /* Front card */
  .front .band {
    position: absolute; left: 0; right: 0; top: 96px; height: 208px;
    background: var(--white);
    border-top: 8px solid var(--blue-bright);
    border-bottom: 8px solid var(--blue-bright);
  }
  .brand {
    position: absolute; display: flex; flex-direction: column; align-items: flex-start;
  }
  .front .brand { left: 50%; top: 50%; transform: translate(-50%, -50%); }
  .brand-name {
    font-weight: 800; font-size: 72px; line-height: .95; letter-spacing: 2px;
    color: var(--navy); white-space: nowrap;
  }
  .brand-sub {
    font-weight: 500; font-size: 15px; letter-spacing: 1.6px;
    color: var(--blue); margin: 6px 0 6px 40px; white-space: nowrap;
  }
  .brand-tag {
    font-weight: 700; font-size: 14px; letter-spacing: .5px;
    background: var(--navy); color: var(--white);
    padding: 3px 10px; margin-left: 28px; white-space: nowrap;
  }

  /* Back card */
  .back .photo {
    position: absolute; top: 0; right: 0; width: 420px; height: 100%;
    background:
      linear-gradient(90deg, var(--navy) 0%, rgba(15,35,80,0) 35%),
      linear-gradient(180deg, #24375e 0%, var(--machine) 30%, #8a6a2e 55%, var(--rock) 75%, #4b525c 100%);
  }
  .back .brand { left: 40px; top: 62px; }
  .back .brand-name { color: var(--white); font-size: 66px; }
  .back .brand-tag { background: var(--white); color: var(--navy); }
  .contact { position: absolute; left: 40px; bottom: 30px; }
  .person {
    font-weight: 800; font-size: 26px; letter-spacing: 1.5px; text-transform: uppercase;
    color: var(--white); margin-bottom: 8px; white-space: nowrap;
  }
  .person .first { color: var(--blue-bright); margin-right: 8px; }
  .contact-list { list-style: none; }
  .contact-list li {
    display: flex; align-items: center; gap: 14px; white-space: nowrap;
    color: var(--white); font-size: 18px; font-weight: 500; margin-top: 6px;
  }
  .icon {
    width: 30px; height: 30px; background: var(--blue);
    display: flex; align-items: center; justify-content: center; flex: none;
  }
  .icon svg { width: 18px; height: 18px; fill: var(--white); }
</style>
</head>
<body>
<main class="sheet">

  <section class="card front">
    <div class="band"></div>
    <div class="brand">
      <span class="brand-name">IRONVALE</span>
      <span class="brand-sub">MAINTENANCE SERVICES PTY LTD</span>
      <span class="brand-tag">MOBILE EQUIPMENT REPAIR AND MAINTENANCE</span>
    </div>
  </section>

  <section class="card back">
    <div class="photo" role="img" aria-label="Photo of a yellow excavator with its bucket resting on a pile of grey rock"></div>
    <div class="brand">
      <span class="brand-name">IRONVALE</span>
      <span class="brand-sub">MAINTENANCE SERVICES PTY LTD</span>
      <span class="brand-tag">MOBILE EQUIPMENT REPAIR AND MAINTENANCE</span>
    </div>
    <div class="contact">
      <p class="person"><span class="first">Derek</span>Holloway</p>
      <ul class="contact-list">
        <li><span class="icon"><svg viewBox="0 0 24 24"><path d="M6.6 10.8a15.1 15.1 0 0 0 6.6 6.6l2.2-2.2a1 1 0 0 1 1-.25 11.4 11.4 0 0 0 3.6.57 1 1 0 0 1 1 1V20a1 1 0 0 1-1 1A17 17 0 0 1 3 4a1 1 0 0 1 1-1h3.5a1 1 0 0 1 1 1c0 1.250.2 2.45.57 3.57a1 1 0 0 1-.25 1z"/></svg></span>043-812-0957</li>
        <li><span class="icon"><svg viewBox="0 0 24 24"><path d="M3 5h18v14H3z M4.5 6.5v.4l7.5 5.6 7.5-5.6v-.4z" fill-rule="evenodd"/></svg></span>derek@ironvalemx.com</li>
        <li><span class="icon"><svg viewBox="0 0 24 24"><path d="M12 2a7 7 0 0 0-7 7c0 5.25 7 13 7 13s7-7.750 7-13a7 7 0 0 0-7-7zm0 9.5A2.5 2.5 0 1 1 12 6.5a2.5 2.5 0 0 1 0 5z"/></svg></span>57 Tarrowby RD Wendale Norvick QX.</li>
      </ul>
    </div>
  </section>

</main>
</body>
</html>
```